Morquent construction chemical business need advertisement

We need an advertisement as building signboard for a new company called "Morquent"-meaning truly effective, value added building solution.
-we source the best and effective products around the world that suit the local climate conditions
- we carry varieties of quality construction chemicals products that are cost effective and suitable for any size of budget and project and even for home user DIY .
- we provide consultation and system to solve any building problems. e.g. tiling system, waterproofing system, concrete repair system, green roof system
- We provide products training and waterproofing solutions to our clients and applicators that use our products
-By utilising our products and services, will leverage the value of the properties and protect your investment.
-our mission- to provide consultancy, services to repair, to restpre and to add avlue to properties throughout the lifecycle of the building resulting in greater whole value hence not limited to develiper but to end user protecting their investment with the quality products and services we provide.
- our philosophy-"Passion towards commitment, quality, knowledge, good practice and result.
- we need the advertisement to be easily understand by End user and contractor of the service and product we provide to solve their problem
- yet also look professional to designer and architect
Target Market(s)
end user, contractor, builder, designer, achitect
Industry/Entity Type
Business
Requirements
Must have
- -Please create a slogan, easily to understand at one glance of what type of service and products we provide.
- -less wording, the advertisement will be put at the building
- -Strong message to explain our business

```html
<!DOCTYPE html>
<html lang="en">
<head>
<meta charset="UTF-8">
<title>Morquent Construction – Flyer</title>
<link href="https://fonts.googleapis.com/css2?family=Anton&family=Open+Sans:wght@400;600;700&display=swap" rel="stylesheet">
<style>
  :root{
    --red:#d3202a;
    --red-bright:#e8232b;
    --yellow:#f7e249;
    --charcoal:#4a4a4a;
    --paper:#f1f1f3;
    --ink:#1c1c1c;
    --stage:#dcdcde;
  }
  *{margin:0;padding:0;box-sizing:border-box}
  html,body{width:1200px;height:1200px;overflow:hidden;background:var(--stage)}
  .flyer{position:absolute;left:190px;top:30px;width:820px;height:1140px;background:var(--paper);overflow:hidden;font-family:"Open Sans",Arial,sans-serif;color:var(--ink);box-shadow:0 10px 30px rgba(0,0,0,.15)}
  .flyer__art{position:absolute;inset:0}
  .brand{position:absolute;right:36px;top:100px;text-align:right;font-family:"Anton",Impact,sans-serif;line-height:1}
  .brand__name{color:#fff;font-size:86px;letter-spacing:1px}
  .brand__sub{color:var(--yellow);font-size:52px;margin-top:4px}
  .slogan{position:absolute;left:530px;top:482px;width:270px;text-align:center}
  .slogan__line{font-family:"Anton",Impact,sans-serif;font-size:54px;line-height:1.05}
  .slogan__line--dark{color:var(--ink)}
  .slogan__line--red{color:var(--red)}
  .slogan__sub{font-size:22px;line-height:1.25;margin-top:10px}
  .tab{position:absolute;height:44px;background:var(--red);color:var(--yellow);font-weight:600;font-size:27px;line-height:44px;box-shadow:0 4px 8px rgba(0,0,0,.15)}
  .tab--about{left:0;top:560px;width:270px;padding-left:40px;border-radius:0 22px 22px 0}
  .tab--mission{right:0;top:716px;width:270px;padding-left:46px;border-radius:22px 0 0 22px}
  .tab--philosophy{right:0;top:924px;width:290px;padding-left:40px;border-radius:22px 0 0 22px}
  .about{position:absolute;left:34px;top:630px;width:470px;list-style:none;font-size:14.5px;line-height:1.4}
  .about li{position:relative;padding-left:14px;margin-bottom:14px}
  .about li::before{content:"";position:absolute;left:0;top:8px;width:5px;height:5px;border-radius:50%;background:var(--red)}
  .mission{position:absolute;left:530px;top:772px;width:270px;font-size:13px;line-height:1.4;text-align:justify;text-align-last:right}
  .philosophy{position:absolute;left:530px;top:980px;width:270px;font-size:13px;line-height:1.4;text-align:center}
  .philosophy p+p{margin-top:8px}
  .site{position:absolute;left:40px;top:1070px;color:#fff;font-size:15px}
  .partners{position:absolute;right:36px;top:1116px;display:flex;gap:26px;align-items:center}
  .partner{display:flex;align-items:center;gap:6px;color:#fff;font-weight:700;font-size:14px}
  .partner__mark{width:12px;height:12px;background:var(--yellow)}
</style>
</head>
<body>
<div class="flyer">
  <svg class="flyer__art" viewBox="0 0 820 1140" width="820" height="1140">
    <defs>
      <linearGradient id="tileTones" x1="0" y1="0" x2="1" y2="1">
        <stop offset="0" stop-color="#c9a37a"/>
        <stop offset=".5" stop-color="#a8764c"/>
        <stop offset="1" stop-color="#6f6a66"/>
      </linearGradient>
    </defs>
    <rect x="520" y="300" width="290" height="400" rx="34" fill="var(--yellow)"/>
    <path d="M0 0 H820 V398 C620 230 330 118 0 128 Z" fill="var(--red)"/>
    <path d="M0 128 C330 118 620 230 820 398 L820 418 C620 252 330 146 0 156 Z" fill="#fff"/>
    <path d="M0 156 C330 146 620 252 820 418 L820 468 C630 300 340 186 0 196 Z" fill="var(--charcoal)"/>
    <path d="M0 204 C300 190 500 240 620 400 C480 290 330 268 0 300 Z" fill="var(--red)"/>
    <circle cx="292" cy="372" r="206" fill="var(--yellow)"/>
    <circle cx="300" cy="380" r="196" fill="var(--red)"/>
    <circle cx="292" cy="378" r="186" fill="url(#tileTones)" role="img" aria-label="Photo of a gloved hand setting ceramic wall tiles onto notched adhesive"/>
    <path d="M0 940 C300 1040 600 1090 820 1100 V1140 H0 Z" fill="var(--yellow)"/>
    <path d="M0 956 C300 1056 600 1104 820 1112 V1140 H0 Z" fill="var(--red-bright)"/>
  </svg>

  <div class="brand">
    <div class="brand__name">MORQUENT</div>
    <div class="brand__sub">CONSTRUCTION</div>
  </div>

  <div class="slogan">
    <div class="slogan__line slogan__line--dark">IF YOU DO IT</div>
    <div class="slogan__line slogan__line--red">DO IT RIGHT</div>
    <p class="slogan__sub">Everything you need<br>from start to finish</p>
  </div>

  <div class="tab tab--about">About Us</div>
  <ul class="about">
    <li>We source the best and effective products around the world that suit the local climate conditions.</li>
    <li>We carry varieties of quality construction chemicals products that are cost effective and suitable for any size of budget and project and even for home user DIY.</li>
    <li>We provide consultation and system to solve any building problems. e.g. tiling system, waterproofing system, concrete repair system, green roof system.</li>
    <li>We provide products training and waterproofing solutions to our clients and applicators that use our products.</li>
    <li>By utilising our products and services, will leverage the value of the properties and protect your investment.</li>
  </ul>

  <div class="tab tab--mission">Our Mission</div>
  <p class="mission">To provide consultancy, services to repair, to restpre and to add avlue to properties throughout the lifecycle of the building resulting in greater whole value hence not limited to develiper but to end user protecting their investment with the quality products and services we provide.</p>

  <div class="tab tab--philosophy">Our Philosophy</div>
  <div class="philosophy">
    <p>Passion towards commitment, quality, knowledge, good practice and result.</p>
    <p>We need the advertisement to be easily understand by End user and contractor of the service and product we provide to solve their problem</p>
  </div>

  <div class="site">www.morquent-build.com</div>
  <div class="partners">
    <span class="partner"><span class="partner__mark"></span>Veltrabond</span>
    <span class="partner">Quarn</span>
    <span class="partner">Ostrel</span>
  </div>
</div>
</body>
</html>
```